Etiketten-Design für Rotwein
Zielgruppe
Weinkellerei aus Baden (Deutschland) mit Fokus im Lebensmittelhandel in Deutschland
Aufgabenstellung
Wir suchen ein Frontetikett für einen modernen badischen Rotwein (Cuvée Noir) mit dem Namen 'The ember hour of Wielgrund'
Aus dem Etikett soll hervorgehen, dass es sich nicht um einen klassischen, leichten deutschen Rotwein handelt, sondern um einen kräftigen, gehaltvollen, mediterran anmutenden Rotwein mit purpurroter Farbe und vollmundigem, nachhaltigem Geschmack. (Geschmacksrichtung feinherb)
Zielgruppe Discount-Kunden, Männlich/Weiblich, Alter: 25-60 Jahre, wird für unter € 5,-/Fl. verkauft.
Weinbeschreibung:
Farbe: Ein wunderschönes tiefdunkles purpurrot mit violetten Reflexen
Duft: In der Nase zeigen sich Aromen nach Waldbeeren, sowie Anklänge von Rauch, Röstaromen, Nelke, etwas Vanille und dunkle Schokolade
Geschmack: Geschmacklich füllig und kraftvoll, Brombeeraromen und schön eingebundenen Tanninen. Langanhaltend intensiv im Abgang.
Anforderungen Etikett:
Maße: Höhe max. 120mm/Breite max. 80mm (darf auch kleiner oder quadratisch sein)
SK Etikett, Naturstruktur bis 90g (m²) (Ein - oder zweiteilig)
Eine figürliche Etikettenkontur ist möglich, es wird aber am rechten Etikettenrand eine gerade Spendekante benötigt um das Etikett maschinell verarbeiten zu können.
Als Flasche wird eine 0,75 L Bordeauxflasche (Farbe: grün) eingesetzt.
Verschluss: Longcap
Mögliche Veredelungen: Quelllack, Prägungen, Heissfolie, Glanzlack
Pflichtangaben:
The ember hour of Wielgrund

```html
<!DOCTYPE html>
<html lang="de">
<head>
<meta charset="utf-8">
<title>The ember hour of Wielgrund – Frontetikett</title>
<link rel="stylesheet" href="https://fonts.googleapis.com/css2?family=Bodoni+Moda:wght@400&display=swap">
<style>
  :root {
    --paper: #ffffff;
    --label-black: #000000;
    --gold: #d6c29c;
    --wine: #6a2d42;
    --dot: #5f2a3d;
  }
  html, body {
    margin: 0;
    padding: 0;
    width: 1137px;
    height: 1200px;
    overflow: hidden;
    background: var(--paper);
  }
  .canvas {
    position: relative;
    width: 1137px;
    height: 1200px;
    background: var(--paper);
  }
  .label {
    position: absolute;
    left: 180px;
    top: 100px;
    width: 778px;
    height: 1000px;
    background: var(--label-black);
    font-family: "Bodoni Moda", "Libre Baskerville", serif;
    font-weight: 400;
  }
  .label__dot {
    position: absolute;
    left: 0;
    top: 477px;
    width: 100px;
    height: 100px;
  }
  .label__title {
    position: absolute;
    left: 274px;
    top: 430px;
    margin: 0;
    font-weight: 400;
    line-height: 1;
    white-space: nowrap;
  }
  .label__article {
    font-size: 37px;
    color: var(--wine);
  }
  .label__name {
    font-size: 92px;
    color: var(--gold);
  }
  .label__subline {
    display: block;
    margin-top: 12px;
    font-size: 37px;
    letter-spacing: 0.02em;
    color: var(--wine);
  }
  .label__vintage {
    position: absolute;
    left: 397px;
    top: 916px;
    transform: translate(-50%, -50%) rotate(-90deg);
    font-size: 32px;
    letter-spacing: 0.02em;
    color: var(--wine);
    white-space: nowrap;
  }
</style>
</head>
<body>
  <main class="canvas">
    <section class="label" aria-label="Frontetikett The ember hour of Wielgrund">
      <svg class="label__dot" viewBox="0 0 100 100" aria-hidden="true">
        <circle cx="50" cy="50" r="50" fill="var(--dot)"/>
      </svg>
      <h1 class="label__title">
        <span class="label__article">the</span> <span class="label__name">ember</span>
        <span class="label__subline">hour of Wielgrund</span>
      </h1>
      <p class="label__vintage">2020</p>
    </section>
  </main>
</body>
</html>
```